Moroccan Taste Colour box Graphic

we need a colour box, with an Arabian Door , as attached and to be called "Gilded Lantern" we would need the box to reveal a Moroccan feel and suggest to use some of the theme of the Black lustre with arabesque designs in Gold. we will need the box front to show life pictures of a Tajine, and a couscous full plate to demonstrate the use of the Argan OIL
The first set will contain: 1 Argan Oil and one Olive oil with hot chili, the second set will contain: one Argan oil and 2 pots of paste Tapenade(Black) and Harissa the third set will contain: 4 paste 1 Harissa Chili, 1 Tapenade Green one Tapenade Black , 1 Lemon Confit
the box contents will be featured on the box sides The box Dimensions are: 8" X 4" X 12" high

Target Market(s)

Culinary foodies,

Font styles to use
Serif

Requirements
Must have
• Moroccan feel, Life pictures to enhance
Nice to have
• Additional proposals for Arabian feel

```html
<!DOCTYPE html>
<html lang="en">
<head>
<meta charset="utf-8">
<title>Gilded Lantern – Colour Box Panels</title>
<link rel="stylesheet" href="https://fonts.googleapis.com/css2?family=Comfortaa:wght@700&display=swap">
<style>
  :root {
    --stage: #5a5a5a;
    --stage-dark: #4a4a4a;
    --lustre-black: #0d0b08;
    --lustre-mid: #2a2417;
    --gold-light: #f6e7a6;
    --gold: #d9b85a;
    --gold-deep: #a8842e;
    --door-grey: #6b6b6b;
    --door-grey-dark: #4f4f4f;
    --tagine-brown: #7a4a22;
    --couscous-gold: #c89a4c;
    --table-wood: #8a7a66;
    --plate-cream: #e6ddcc;
  }
  * { margin: 0; padding: 0; box-sizing: border-box; }
  html, body { width: 1200px; height: 852px; overflow: hidden; }
  body {
    background: radial-gradient(ellipse at center, var(--stage) 0%, var(--stage-dark) 100%);
    position: relative;
    font-family: "Comfortaa", sans-serif;
  }
  .box-panel { position: absolute; top: 39px; height: 781px; }
  .box-panel svg { display: block; width: 100%; height: 100%; }
  .side-left { left: 33px; width: 260px; }
  .front { left: 343px; width: 520px; }
  .side-right { left: 912px; width: 260px; }

  .brand {
    position: absolute;
    left: 0; right: 0;
    text-align: center;
    font-weight: 700;
    line-height: 0.95;
    background: linear-gradient(180deg, var(--gold-light) 0%, var(--gold) 55%, var(--gold-deep) 100%);
    -webkit-background-clip: text;
    background-clip: text;
    color: transparent;
    filter: drop-shadow(0 2px 2px rgba(0,0,0,0.6));
  }
  .brand .brand-top { display: block; }
  .brand .brand-main { display: block; }
  .side-left .brand, .side-right .brand { top: 322px; }
  .side-left .brand-top, .side-right .brand-top { font-size: 21px; }
  .side-left .brand-main, .side-right .brand-main { font-size: 34px; }
  .front .brand { top: 16px; }
  .front .brand-top { font-size: 32px; }
  .front .brand-main { font-size: 52px; }
</style>
</head>
<body>
  <svg width="0" height="0" style="position:absolute">
    <defs>
      <linearGradient id="gold-band" x1="0" y1="0" x2="1" y2="1">
        <stop offset="0" stop-color="#f6e7a6"/>
        <stop offset="0.5" stop-color="#d9b85a"/>
        <stop offset="1" stop-color="#a8842e"/>
      </linearGradient>
      <radialGradient id="lustre" cx="0.5" cy="0.5" r="0.7">
        <stop offset="0" stop-color="#2a2417"/>
        <stop offset="1" stop-color="#0d0b08"/>
      </radialGradient>
      <linearGradient id="tagine-photo" x1="0" y1="0" x2="1" y2="1">
        <stop offset="0" stop-color="#b7a68c"/>
        <stop offset="0.5" stop-color="#7a4a22"/>
        <stop offset="1" stop-color="#4a2c14"/>
      </linearGradient>
      <linearGradient id="couscous-photo" x1="0" y1="0" x2="1" y2="1">
        <stop offset="0" stop-color="#e8d9b4"/>
        <stop offset="0.5" stop-color="#d49a4a"/>
        <stop offset="1" stop-color="#c89a4c"/>
      </linearGradient>
      <linearGradient id="plate-photo" x1="0" y1="0" x2="1" y2="1">
        <stop offset="0" stop-color="#e6ddcc"/>
        <stop offset="0.5" stop-color="#c9a060"/>
        <stop offset="1" stop-color="#b9b2a6"/>
      </linearGradient>
      <linearGradient id="pot-photo" x1="0" y1="0" x2="1" y2="1">
        <stop offset="0" stop-color="#8a7a66"/>
        <stop offset="0.6" stop-color="#4a3a2a"/>
        <stop offset="1" stop-color="#c8501e"/>
      </linearGradient>
      <linearGradient id="feast-photo" x1="0" y1="0" x2="1" y2="0">
        <stop offset="0" stop-color="#6a4a2a"/>
        <stop offset="0.45" stop-color="#8a6a3a"/>
        <stop offset="1" stop-color="#b87a3a"/>
      </linearGradient>
      <radialGradient id="door" cx="0.5" cy="0.35" r="0.7">
        <stop offset="0" stop-color="#6b6b6b"/>
        <stop offset="1" stop-color="#4f4f4f"/>
      </radialGradient>
    </defs>
  </svg>

  <section class="box-panel side-left">
    <svg viewBox="0 0 260 781" aria-hidden="false">
      <rect class="lustre-pattern" role="img" aria-label="Black lustre background with gold arabesque star pattern" width="260" height="781" fill="url(#lustre)"/>
      <path class="photo" role="img" aria-label="Photo of a beef and apricot tajine in a terracotta dish" d="M0 0 H260 V263 Q120 250 0 172 Z" fill="url(#tagine-photo)"/>
      <path class="gold-curve" d="M0 172 Q120 250 260 263 V272 Q115 260 0 181 Z" fill="url(#gold-band)"/>
      <path class="photo" role="img" aria-label="Photo of a couscous plate with chicken, chickpeas and vegetables" d="M0 533 Q150 530 260 630 V781 H0 Z" fill="url(#plate-photo)"/>
      <path class="gold-curve" d="M0 525 Q155 522 260 622 V632 Q150 532 0 535 Z" fill="url(#gold-band)"/>
    </svg>
    <div class="brand"><span class="brand-top">Gilded</span><span class="brand-main">Lantern</span></div>
  </section>

  <section class="box-panel front">
    <svg viewBox="0 0 520 781">
      <rect class="lustre-pattern" role="img" aria-label="Black lustre background with gold arabesque star pattern" width="520" height="781" fill="url(#lustre)"/>
      <path class="photo" role="img" aria-label="Photo of a vegetable tajine beside a full couscous plate with merguez and carrots" d="M0 0 H520 V318 Q470 340 420 335 L100 335 Q40 330 0 310 Z" fill="url(#feast-photo)"/>
      <path class="gold-curve" d="M0 310 Q40 330 100 335 L420 335 Q470 340 520 318 V326 Q470 348 420 343 L100 343 Q40 338 0 318 Z" fill="url(#gold-band)"/>
      <path class="arabian-door" d="M60 720 L60 430 C60 415 75 410 88 405 C70 385 60 355 70 320 C85 265 150 230 200 200 C235 180 255 140 260 106 C265 140 285 180 320 200 C370 230 435 265 450 320 C460 355 450 385 432 405 C445 410 460 415 460 430 L460 720 Z" fill="url(#door)" stroke="url(#gold-band)" stroke-width="9" stroke-linejoin="miter"/>
    </svg>
    <div class="brand"><span class="brand-top">Gilded</span><span class="brand-main">Lantern</span></div>
  </section>

  <section class="box-panel side-right">
    <svg viewBox="0 0 260 781">
      <rect class="lustre-pattern" role="img" aria-label="Black lustre background with gold arabesque star pattern" width="260" height="781" fill="url(#lustre)"/>
      <path class="photo" role="img" aria-label="Photo of couscous topped with carrots, pumpkin, chickpeas and a green chili" d="M0 0 H260 V184 Q140 250 0 254 Z" fill="url(#couscous-photo)"/>
      <path class="gold-curve" d="M0 254 Q140 250 260 184 V193 Q140 260 0 263 Z" fill="url(#gold-band)"/>
      <path class="photo" role="img" aria-label="Photo of a black tajine pot with lamb and potatoes beside an orange tajine lid" d="M0 630 Q110 530 260 533 V781 H0 Z" fill="url(#pot-photo)"/>
      <path class="gold-curve" d="M0 622 Q105 522 260 525 V535 Q110 532 0 632 Z" fill="url(#gold-band)"/>
    </svg>
    <div class="brand"><span class="brand-top">Gilded</span><span class="brand-main">Lantern</span></div>
  </section>
</body>
</html>
```